幼稚園で行う文化祭のようなイベントのPR広告のデザインをお願いしたいです。 サイズは横119㎜×縦95㎜の変形サイズで片面フルカラーです。 デザインは、ポップでかわいい目につくような感じで色合いは、パステルカラーを基調にしてほしいですが、パリッとした色も入れてほしいです。・ぽかぽかまつり、日付を大きく・イベント内容の〈お話ボックス〉と〈美味しいお店〉の大きさは、お話ボックスの方少し大きくしてほしいです。・ぷくりん商店さん写真(あんみつ)にぷくりん商店さんのロゴを乗せていただいたいです。・屋号部分に、若葉台学院附属幼稚園のロゴを起用。ロゴのイラストは入れれたらいれていただきたいです。入らない場合は、入れなくてOKです。・地図は、ハッピーマート若葉台学院附属高校前、青葉野南郵便局をいれていただき、若葉台学院附属高校の建物と、その奥の3つの建物のも入れていただきたいです。昨年の原稿の地図を参考にしていただけますと幸いです。 諸々使用いただきたい素材と、昨年の原稿(デザインはガラッと変えてほしいです)を下記にアップいたしましたのでご確認いただけますと幸いです。 https://42.filebox-share.jp/0923-ab47ce1193fd82a61e57bc0de93214cdf その他ご質問等ありましたら、気軽にお問い合わせください。 ご応募をお待ちしております! |
どの案も素敵でしたがこちらの案がイメージと近く、採用させていただきました
皆さまご提案ありがとうございました。
素晴らしいデザインばかりでとてもありがとうございました。
今後もこのような機会がございましたらご提案いただけますと幸いです。

```html
<!DOCTYPE html>
<html lang="ja">
<head>
<meta charset="utf-8">
<title>ぽかぽかまつり</title>
<link rel="stylesheet" href="https://fonts.googleapis.com/css2?family=M+PLUS+Rounded+1c:wght@500;700;800&family=Kiwi+Maru:wght@500&display=swap">
<style>
:root{
  --sky:#dcecf7;
  --navy:#2c4a7a;
  --teal:#3aa8a0;
  --label:#f7e47c;
  --hill:#c6e6cf;
  --hill-deep:#a9d8b6;
  --red:#e0473a;
  --ink:#2b3440;
  --brown:#6b4a2e;
  --white:#ffffff;
}
*{margin:0;padding:0;box-sizing:border-box}
html,body{width:1200px;height:957px;overflow:hidden;background:var(--sky)}
.flyer{position:relative;width:1200px;height:957px;overflow:hidden;background:var(--sky);font-family:"M PLUS Rounded 1c",sans-serif;color:var(--ink)}
.abs{position:absolute}
.date-badge{left:-106px;top:-106px;width:340px;height:340px;border-radius:50%;background:var(--navy)}
.date-day{left:22px;top:14px;font-size:84px;font-weight:800;line-height:1;color:var(--white);letter-spacing:-2px}
.date-week{left:136px;top:120px;width:42px;height:42px;border-radius:50%;background:var(--white);color:var(--navy);font-size:25px;font-weight:800;display:flex;align-items:center;justify-content:center}
.date-time{left:28px;top:124px;font-size:34px;font-weight:700;line-height:1.25;color:var(--white)}
.subtitle{left:0;width:1200px;top:20px;text-align:center;font-size:24px;font-weight:700;color:var(--navy)}
.edition{left:510px;top:76px;width:180px;height:46px;background:var(--teal);color:var(--white);border-radius:8px;font-size:30px;font-weight:800;display:flex;align-items:center;justify-content:center}
.title{left:0;width:1200px;top:126px;text-align:center;font-family:"Kiwi Maru",serif;font-weight:500;font-size:88px;color:var(--navy);letter-spacing:6px;line-height:1.1}
.shops-lead{left:443px;width:670px;top:262px;text-align:center;font-size:20px;font-weight:700;color:var(--navy)}
.story-label{left:145px;top:298px;width:280px;height:44px;border-radius:22px;background:var(--teal);color:var(--white);font-size:26px;font-weight:800;display:flex;align-items:center;justify-content:center}
.story-photo{left:170px;top:366px;width:240px;height:294px;border-radius:6px;background:linear-gradient(160deg,#f4e6a6,#9fc7e6);box-shadow:0 3px 0 rgba(0,0,0,.12)}
.story-text{left:100px;width:380px;top:672px;text-align:center;font-size:20px;font-weight:700;line-height:1.5;color:var(--navy)}
.shop{width:208px}
.shop-kind{text-align:center;font-size:18px;font-weight:700;color:var(--ink);margin-bottom:8px;line-height:1.2}
.shop-photo{height:120px;border-radius:4px}
.shop-name{margin:-14px auto 0;position:relative;width:156px;height:44px;background:var(--label);border-radius:4px;text-align:center;font-size:21px;font-weight:800;display:flex;align-items:center;justify-content:center;line-height:1.1}
.shop-name.dark{background:#2b2b2b;color:var(--white);font-size:14px}
.hill{left:0;top:700px;width:1200px;height:260px}
.deco{border-radius:50%}
.school-mark{left:44px;top:800px;font-size:15px;font-weight:700;color:var(--brown)}
.school{left:42px;top:822px;font-size:36px;font-weight:800;color:var(--brown);letter-spacing:1px;line-height:1.2}
.phone{left:80px;top:888px;font-size:27px;font-weight:800;color:var(--ink);display:flex;align-items:center;gap:8px}
.divider{left:575px;top:795px;width:2px;height:140px;background:#8aa}
.address{left:598px;top:808px;font-size:23px;font-weight:700;line-height:1.45;color:var(--ink)}
.parking{left:598px;top:880px;font-size:20px;font-weight:700;line-height:1.4;color:var(--red)}
.map{left:936px;top:787px;width:214px;height:150px;border-radius:6px;background:#eef1ea;border:2px solid #fff}
</style>
</head>
<body>
<main class="flyer">
  <div class="abs deco" role="img" aria-label="気球のイラスト" style="left:0;top:290px;width:44px;height:58px;background:#f1a6a0"></div>
  <div class="abs deco" role="img" aria-label="気球のイラスト" style="left:16px;top:420px;width:40px;height:52px;background:#f5b1a8"></div>
  <div class="abs deco" role="img" aria-label="気球のイラスト" style="left:1150px;top:390px;width:50px;height:66px;background:#f4d483"></div>
  <div class="abs deco" role="img" aria-label="カラフルな花と模様の装飾" style="left:1010px;top:-20px;width:220px;height:230px;background:radial-gradient(circle,#f6c75d,#e98aa8 55%,#8ec9e0)"></div>

  <div class="abs date-badge"></div>
  <div class="abs date-day">11/9</div>
  <div class="abs date-time">10:00<br>-14:00</div>
  <div class="abs date-week">日</div>

  <p class="abs subtitle">楽しい親子で遊ぼう</p>
  <div class="abs edition">第3回</div>
  <h1 class="abs title">ぽかぽかまつり</h1>
  <p class="abs shops-lead">美味しいお店もやってくる！</p>

  <svg class="abs hill" viewBox="0 0 1200 260" preserveAspectRatio="none" aria-hidden="true">
    <path d="M0 30 C300 0 900 -10 1200 20 L1200 260 L0 260Z" fill="var(--hill)"/>
    <path d="M0 75 C400 40 800 45 1200 70" fill="none" stroke="var(--hill-deep)" stroke-width="3"/>
  </svg>
  <div class="abs" role="img" aria-label="親子のイラスト" style="left:10px;top:600px;width:70px;height:140px;border-radius:30px;background:#f2b8a0"></div>
  <div class="abs" role="img" aria-label="子どものイラスト" style="left:1150px;top:630px;width:44px;height:100px;border-radius:20px;background:#9fc7e6"></div>

  <div class="abs story-label">お話ボックス</div>
  <div class="abs story-photo" role="img" aria-label="おはなしぼっくすの手作り看板の写真"></div>
  <p class="abs story-text">若葉台学院大学生のお兄さん・<br>お姉さんと一緒に遊ぼう</p>

  <section class="abs shop" style="left:443px;top:320px"><p class="shop-kind">焼きうどん</p><div class="shop-photo" role="img" aria-label="焼きうどんの写真" style="background:linear-gradient(#d9c79a,#8a8f5c)"></div><p class="shop-name">大福亭</p></section>
  <section class="abs shop" style="left:677px;top:320px"><p class="shop-kind">ピザ・コーヒー等</p><div class="shop-photo" role="img" aria-label="ピザとドリンクの写真" style="background:linear-gradient(#7a4a30,#c98a4a)"></div><p class="shop-name">ルーチェ</p></section>
  <section class="abs shop" style="left:905px;top:320px"><p class="shop-kind">プリン・あんみつ</p><div class="shop-photo" role="img" aria-label="あんみつとプリンの写真" style="background:linear-gradient(#f3e7d8,#c98da0)"></div><p class="shop-name">ぷくりん商店</p></section>
  <section class="abs shop" style="left:443px;top:556px"><p class="shop-kind">お団子</p><div class="shop-photo" role="img" aria-label="お団子の写真" style="background:linear-gradient(#c99a5a,#8a5a2a)"></div><p class="shop-name">さとのや</p></section>
  <section class="abs shop" style="left:677px;top:556px"><p class="shop-kind">メンチカツバーガー</p><div class="shop-photo" role="img" aria-label="キッチンカーの写真" style="background:linear-gradient(#5a5a5a,#2a2a2a)"></div><p class="shop-name dark">BISTRO<br>MAISON CLAIR</p></section>
  <section class="abs shop" style="left:905px;top:556px"><p class="shop-kind">ホットドック等</p><div class="shop-photo" role="img" aria-label="ホットドッグのキッチンカーの写真" style="background:linear-gradient(#d8c48a,#6a7a4a)"></div><p class="shop-name">Happy Oink</p></section>

  <p class="abs school-mark">幼保連携型認定こども園</p>
  <p class="abs school">若葉台学院附属幼稚園</p>
  <p class="abs phone"><svg width="26" height="26" viewBox="0 0 24 24" aria-hidden="true"><path d="M6.6 10.8a15 15 0 0 0 6.6 6.6l2.2-2.2a1 1 0 0 1 1-.25 11.4 11.4 0 0 0 3.6.57 1 1 0 0 1 1 1V20a1 1 0 0 1-1 1A17 17 0 0 1 3 4a1 1 0 0 1 1-1h3.5a1 1 0 0 1 1 1c0 1.25.2 2.45.57 3.6a1 1 0 0 1-.25 1z" fill="var(--ink)"/></svg>019-000-4821</p>

  <div class="abs divider"></div>
  <p class="abs address"><svg width="22" height="26" viewBox="0 0 24 28" style="vertical-align:-4px" aria-hidden="true"><path d="M12 0a10 10 0 0 0-10 10c0 7.5 10 18 10 18s10-10.5 10-18A10 10 0 0 0 12 0zm0 14a4 4 0 1 1 0-8 4 4 0 0 1 0 8z" fill="var(--teal)"/></svg> 〒000-0124<br>若葉市青葉野５丁目４－１</p>
  <p class="abs parking">駐車場は若葉台学院附属高校前<br>をお使いください。</p>
  <div class="abs map" role="img" aria-label="会場周辺地図：若葉台学院附属高校、ハッピーマート若葉台学院附属高校前、青葉野南郵便局"></div>
</main>
</body>
</html>
```